Forge Rankers
Welder Certification
Forge Rankers - Engineering
Creative Brief
Simple
Derek Halloway
QA Manager / SCWI
48213 W 61st Ave Aurora, CO 80017
derek@forgerankers.com
forgerankers.com

```html
<!DOCTYPE html>
<html lang="en">
<head>
<meta charset="utf-8">
<title>Forge Rankers – Business Card Options</title>
<link rel="stylesheet" href="https://fonts.googleapis.com/css2?family=Oswald:wght@600&family=Open+Sans:wght@400;600&display=swap">
<style>
  :root {
    --backdrop: #e9e6e2;
    --card-dark: #2a2a2a;
    --card-light: #ffffff;
    --accent: #f28c1e;
    --text-light: #d9d9d9;
    --text-muted-light: #a8a8a8;
    --text-dark: #3d3d3d;
    --text-muted-dark: #6e6e6e;
    --label-dark: #2b2b2b;
  }
  * { margin: 0; padding: 0; box-sizing: border-box; }
  html, body { width: 1200px; height: 901px; overflow: hidden; }
  body {
    background: var(--backdrop);
    font-family: "Open Sans", Arial, sans-serif;
    position: relative;
  }
  .option-label {
    position: absolute;
    font-size: 26px;
    padding: 10px 22px;
    line-height: 1;
  }
  .option-label--one { left: 0; top: 165px; background: var(--label-dark); color: #fff; }
  .option-label--two { right: 0; top: 470px; background: #fff; color: var(--text-dark); }

  .business-card {
    position: absolute;
    width: 500px;
    height: 286px;
    display: flex;
    flex-direction: column;
    align-items: center;
    justify-content: center;
    text-align: center;
    box-shadow: 0 10px 24px rgba(0,0,0,0.18);
  }
  .business-card--dark { left: 120px; top: 250px; background: var(--card-dark); }
  .business-card--light { left: 580px; top: 560px; background: var(--card-light); }

  .brand {
    display: flex;
    align-items: center;
    gap: 12px;
    margin-bottom: 18px;
  }
  .brand-square {
    width: 26px;
    height: 26px;
    background: var(--accent);
  }
  .brand-name {
    font-family: "Oswald", Arial, sans-serif;
    font-weight: 600;
    font-size: 30px;
    letter-spacing: 1px;
    text-transform: uppercase;
    color: var(--accent);
  }
  .holder-name {
    font-family: "Oswald", Arial, sans-serif;
    font-weight: 600;
    font-size: 24px;
    letter-spacing: 1px;
    text-transform: uppercase;
    color: var(--accent);
  }
  .holder-role {
    font-size: 13px;
    margin-top: 2px;
    margin-bottom: 22px;
  }
  .contact-line {
    font-size: 11px;
    line-height: 1.7;
  }
  .contact-line .divider { margin: 0 6px; }

  .business-card--dark .holder-role { color: var(--text-light); }
  .business-card--dark .contact-line { color: var(--text-muted-light); }
  .business-card--light .holder-role { color: var(--text-dark); }
  .business-card--light .contact-line { color: var(--text-muted-dark); }
</style>
</head>
<body>
  <div class="option-label option-label--one">Option 1</div>
  <div class="option-label option-label--two">Option 2</div>

  <section class="business-card business-card--dark">
    <div class="brand">
      <span class="brand-square"></span>
      <span class="brand-name">Forge Rankers</span>
    </div>
    <div class="holder-name">Derek Halloway</div>
    <div class="holder-role">QA Manager / SCWI</div>
    <div class="contact-line">303-555-0142<span class="divider">|</span>derek@forgerankers.com<span class="divider">|</span>forgerankers.com</div>
    <div class="contact-line">48213 W 61st Ave Aurora, CO 80017</div>
  </section>

  <section class="business-card business-card--light">
    <div class="brand">
      <span class="brand-square"></span>
      <span class="brand-name">Forge Rankers</span>
    </div>
    <div class="holder-name">Derek Halloway</div>
    <div class="holder-role">QA Manager / SCWI</div>
    <div class="contact-line">303-555-0142<span class="divider">|</span>derek@forgerankers.com<span class="divider">|</span>forgerankers.com</div>
    <div class="contact-line">48213 W 61st Ave Aurora, CO 80017</div>
  </section>
</body>
</html>
```